Secretary Business Cards for Golf Club

Hi I need a new business card designed.

I am the secretary at the Carrowen Golf Club - I take care of all the club functions & run the club on a day to day basis.

I don't want golf as the main feature I would like Functions to be the main focus.

Clean Crisp & Professional

Please include the following:

Carrowen Golf Club
Marguerite Vallance Secretary

"Thornby Park"
Bellmoor Ridge Road
WIRRALONG NSW 2795

Ph 02 - 6378 2405
Mobile 0471 326 815

carrowengolfclub@mailnestor.com

www.carrowengolfclub.com.au

```html
<!DOCTYPE html>
<html lang="en">
<head>
<meta charset="utf-8">
<title>Carrowen Golf Club – Secretary Business Card</title>
<link rel="stylesheet" href="https://fonts.googleapis.com/css2?family=Questrial&display=swap">
<style>
  :root {
    --card-bg: #8fa3a0;
    --ink-blue: #0a33c8;
  }
  html, body {
    margin: 0;
    padding: 0;
    width: 1200px;
    height: 702px;
    overflow: hidden;
    background: var(--card-bg);
  }
  .business-card {
    display: block;
    width: 1200px;
    height: 702px;
    background: var(--card-bg);
  }
  .business-card text {
    font-family: "Questrial", "Century Gothic", sans-serif;
    fill: var(--ink-blue);
    text-anchor: middle;
  }
  .club-name { font-size: 101px; }
  .secretary-line { font-size: 53px; }
  .address-line { font-size: 36px; }
  .contact-line { font-size: 34px; }
</style>
</head>
<body>
<svg class="business-card" width="1200" height="702" viewBox="0 0 1200 702" xmlns="http://www.w3.org/2000/svg" aria-label="Carrowen Golf Club secretary business card">
  <text class="club-name" x="588" y="150">Carrowen Golf Club</text>
  <text class="secretary-line" x="590" y="225">Marguerite Vallance Secretary</text>

  <g class="postal-address">
    <text class="address-line" x="580" y="302">"Thornby Park"</text>
    <text class="address-line" x="580" y="350">Bellmoor Ridge Road</text>
    <text class="address-line" x="580" y="399">WIRRALONG NSW 2795</text>
  </g>

  <g class="contact-details">
    <text class="contact-line" x="578" y="494">Ph 02 - 6378 2405</text>
    <text class="contact-line" x="578" y="539">Mobile 0471 326 815</text>
    <text class="contact-line" x="578" y="584">carrowengolfclub@mailnestor.com</text>
    <text class="contact-line" x="578" y="628">www.carrowengolfclub.com.au</text>
  </g>
</svg>
</body>
</html>
```